Boilerplate Management Organization Chart

"Our Management Approach is a deliberate step-by-step process and supports our Technical Approach detailed in proposal submission. The Management Approach covers all the human capital aspects for executing a contract—from contract award through to sustainment and/or transition of the contract to another company. It includes how we organize, hire, staff, train, and account for our contract employees—as well as their complete personal life-cycle management within the company."

We need this management approach to depict an amazing management process that demonstrates best practices of the project management body of knowledge. We need this vector image to be applicable to any proposal without making references to any other proposals. Generic names but using strong business language.
Updates

Thanks for all designs submitted thus far. Some have stuck to the original type of chart. We would like to see a completely different way to show the same information. It has to be able to be recognized and deciphered very quickly by people who might not necessarily want to look at it. It must draw them in and make it incredibly easy to distinguish a management approach that looks fresh, infallible, and easily implemented.

Target Market(s)

Federal space, Government organizations looking for procedural efficiencies,

Industry/Entity Type

Management

Requirements
Must have
• Must not take up more than 1/3 to 1/2 of printable page and be clear.
Should not have
• Not too much color, but should stick to some color palette of some interest.

```html
<!DOCTYPE html>
<html lang="en">
<head>
<meta charset="utf-8">
<title>Management Approach</title>
<link rel="stylesheet" href="https://fonts.googleapis.com/css2?family=Barlow:wght@700&family=Exo+2:ital,wght@1,800&family=Rubik:wght@800&display=swap">
<style>
  :root {
    --page: #ffffff;
    --panel-light: #f2f1ec;
    --panel-dark: #d7d4c8;
    --orange: #f77f00;
    --teal: #14b1a6;
    --label: #5c5c6a;
    --white: #ffffff;
  }
  html, body {
    margin: 0;
    width: 1200px;
    height: 1200px;
    overflow: hidden;
    background: var(--page);
  }
  .canvas { display: block; width: 1200px; height: 1200px; }
  .title { font-family: "Exo 2", sans-serif; font-style: italic; font-weight: 800; fill: var(--white); letter-spacing: 5px; font-size: 37px; }
  .step-number { font-family: "Rubik", sans-serif; font-weight: 800; font-size: 48px; fill: var(--white); }
  .step-label { font-family: "Barlow", sans-serif; font-weight: 700; font-size: 18.5px; fill: var(--label); }
  .footer-label { font-family: "Barlow", sans-serif; font-weight: 700; font-size: 31px; fill: var(--orange); }
  .step-box { fill: var(--teal); }
  .connector { stroke: var(--teal); stroke-width: 2; fill: none; }
  .path-dots { stroke: var(--orange); stroke-width: 2.4; stroke-dasharray: 2 4; fill: none; }
  .node { fill: var(--orange); }
  .footer-bracket { stroke: var(--orange); stroke-width: 2; stroke-dasharray: 2 4; fill: none; }
</style>
</head>
<body>
<svg class="canvas" viewBox="0 0 1200 1200" xmlns="http://www.w3.org/2000/svg">
  <defs>
    <radialGradient id="panelGlow" cx="50%" cy="45%" r="60%">
      <stop offset="0" stop-color="var(--panel-light)"/>
      <stop offset="1" stop-color="var(--panel-dark)"/>
    </radialGradient>
    <filter id="numberShadow" x="-20%" y="-20%" width="140%" height="140%">
      <feDropShadow dx="2" dy="2" stdDeviation="1" flood-color="#0a5e58" flood-opacity="0.55"/>
    </filter>
  </defs>

  <!-- Panel -->
  <rect class="panel" x="177" y="98" width="851" height="1034" fill="url(#panelGlow)"/>

  <!-- Header banner -->
  <g class="header">
    <polygon points="177,124 660,124 618,182 660,241 177,241" fill="var(--orange)"/>
    <g class="target-icon">
      <circle cx="231" cy="180" r="25" fill="none" stroke="var(--white)" stroke-width="8"/>
      <circle cx="231" cy="180" r="9" fill="none" stroke="var(--white)" stroke-width="6"/>
      <polygon points="203,156 226,170 219,176" fill="#6a6a78"/>
    </g>
    <text class="title" x="278" y="174">MANAGEMENT</text>
    <line x1="276" y1="183" x2="572" y2="183" stroke="var(--white)" stroke-width="2.4" stroke-dasharray="1.5 4" stroke-linecap="round"/>
    <text class="title" x="264" y="222">APPROACH</text>
  </g>

  <!-- Zig-zag path -->
  <polyline class="path-dots" points="559,311 666,405 559,494 666,588 559,680 666,782 559,873 666,966"/>

  <!-- Left steps -->
  <g class="steps-left">
    <path class="connector" d="M398 311 H559 M338 358 V428"/>
    <rect class="step-box" x="296" y="266" width="103" height="92" rx="2"/>
    <text class="step-number" x="347" y="330" text-anchor="middle" filter="url(#numberShadow)">01</text>
    <text class="step-label" x="350" y="400">RESPONSIBILITY FIXED</text>

    <path class="connector" d="M398 494 H559 M338 542 V612"/>
    <rect class="step-box" x="296" y="450" width="103" height="92" rx="2"/>
    <text class="step-number" x="347" y="514" text-anchor="middle" filter="url(#numberShadow)">03</text>
    <text class="step-label" x="366" y="584">MANNING THE TEAM</text>

    <path class="connector" d="M398 680 H559 M338 726 V796"/>
    <rect class="step-box" x="296" y="634" width="103" height="92" rx="2"/>
    <text class="step-number" x="347" y="698" text-anchor="middle" filter="url(#numberShadow)">05</text>
    <text class="step-label" x="366" y="756">PROFESSION</text>
    <text class="step-label" x="366" y="780">DEVELOPMENT</text>

    <path class="connector" d="M398 873 H559 M338 918 V990"/>
    <rect class="step-box" x="296" y="826" width="103" height="92" rx="2"/>
    <text class="step-number" x="347" y="890" text-anchor="middle" filter="url(#numberShadow)">07</text>
    <text class="step-label" x="374" y="960">BENEFITS</text>
  </g>

  <!-- Right steps -->
  <g class="steps-right">
    <path class="connector" d="M666 405 H827 M760 289 H894 V358"/>
    <rect class="step-box" x="827" y="358" width="103" height="92" rx="2"/>
    <text class="step-number" x="878" y="422" text-anchor="middle" filter="url(#numberShadow)">02</text>
    <text class="step-label" x="882" y="322" text-anchor="end">MANAGEMENT &amp; OVERSIGHT</text>

    <path class="connector" d="M666 588 H827 M760 475 H894 V542"/>
    <rect class="step-box" x="827" y="542" width="103" height="92" rx="2"/>
    <text class="step-number" x="878" y="606" text-anchor="middle" filter="url(#numberShadow)">04</text>
    <text class="step-label" x="882" y="507" text-anchor="end">TRAINING</text>

    <path class="connector" d="M666 782 H827 M760 664 H894 V735"/>
    <rect class="step-box" x="827" y="735" width="103" height="91" rx="2"/>
    <text class="step-number" x="878" y="799" text-anchor="middle" filter="url(#numberShadow)">06</text>
    <text class="step-label" x="875" y="691" text-anchor="end">RETENTION /</text>
    <text class="step-label" x="875" y="715" text-anchor="end">QUALITY OF LIFE</text>

    <path class="connector" d="M666 966 H827 M760 853 H894 V919"/>
    <rect class="step-box" x="827" y="919" width="103" height="91" rx="2"/>
    <text class="step-number" x="878" y="983" text-anchor="middle" filter="url(#numberShadow)">08</text>
    <text class="step-label" x="877" y="879" text-anchor="end">SUSTAINMENT /</text>
    <text class="step-label" x="877" y="903" text-anchor="end">TRANSITION</text>
  </g>

  <!-- Nodes -->
  <g class="nodes">
    <circle class="node" cx="559" cy="311" r="7.5"/>
    <circle class="node" cx="666" cy="405" r="7.5"/>
    <circle class="node" cx="559" cy="494" r="7.5"/>
    <circle class="node" cx="666" cy="588" r="7.5"/>
    <circle class="node" cx="559" cy="680" r="7.5"/>
    <circle class="node" cx="666" cy="782" r="7.5"/>
    <circle class="node" cx="559" cy="873" r="7.5"/>
    <circle class="node" cx="666" cy="966" r="7.5"/>
  </g>

  <!-- Footer -->
  <g class="footer">
    <path class="footer-bracket" d="M221 998 V1086 H390"/>
    <path class="footer-bracket" d="M814 1086 H986 V994"/>
    <text class="footer-label" x="602" y="1096" text-anchor="middle">PROGRAM DEVELOPMENT</text>
  </g>
</svg>
</body>
</html>
```